Infografiken für Anbieter von Sport-Trainingseinheiten
Zielgruppe
Wir unterstützen und motivieren Menschen regelmässig und Nachhaltig Bewegung und Sport in ihren Alltag zu integrieren. Dafür bieten wir individuelle Trainingseinheiten an, die ganzheitlich, abwechslungsreich sind und Spass machen.
Aufgabenstellung
4 einfache und einheitliche Infografiken im selben Stil für meine neue Webseite
Infografik 1: Was Personal Training ausmacht (Stichworte: motivierend, individuell, flexibel, ganzheitlich und abwechslungsreich)
Infografik 2: Ablauf/Prozess vom Erstgespräch über die Standortbestimmung, Zielsetzung, das Training bis zum Erfolg
Infografik 3: Zwei Säulen des Athletiktrainings: Verletzungsprävention und Leistungssteigerung (beide gleich wichtig)
Infografik 4: Der Prozess eines Athleten von der Ist-Soll-Analyse über Leistungstests, Trainingsplanung, Vorwettkampf bis zum Wettkampf (Weg Treppe - Ziel Trophäe)
Die Infografiken sollen sehr leicht lesbar, verständlich und vom Design her minimalisitisch sein. Eine schlichte, sportliche und elegante Darstellung ist erwünscht. Bei den Designelementen lasse ich mich überraschen. Ich bin offen für Vorschläge.
Farben: Schwarz, Weiss und Grau
Mir ist wichtig, dass die Grafiken denselben Stil haben und einheitlich erschienen.
Meine selbst erstellten Grafiken finden sie auf meiner 'noch' aktuellen Seite unter folgenden Links:
https://www.hb-fitcoaching.ch/personal-training/
https://www.hb-fitcoaching.ch/athletik-training/

```html
<!DOCTYPE html>
<html lang="de">
<head>
<meta charset="utf-8">
<title>HB Fitcoaching – Infografiken</title>
<link rel="stylesheet" href="https://fonts.googleapis.com/css2?family=Crimson+Pro:wght@400&display=swap">
<style>
  :root{
    --ink:#2e2e30;
    --grey:#616163;
    --grey-dark:#3d3d3f;
    --line:#3a3a3a;
    --thin:#8a8a8a;
    --paper:#ffffff;
    --band:#f4f4f4;
    --rule:#e4e4e4;
  }
  *{box-sizing:border-box;margin:0;padding:0}
  html,body{width:1200px;height:3024px;overflow:hidden;background:var(--paper)}
  body{font-family:"Crimson Pro",Georgia,serif;color:var(--ink);position:relative}
  svg text{font-family:"Crimson Pro",Georgia,serif}
  .sprite{position:absolute;width:0;height:0}
  .infographics{position:absolute;left:0;top:0;width:1200px;height:820px}

  .web-page{position:absolute;left:0;top:880px;width:1200px;height:710px;border-top:1px solid var(--rule);border-bottom:1px solid var(--rule);overflow:hidden}
  .site-nav{height:62px;display:flex;align-items:center;justify-content:center;gap:22px;border-bottom:1px solid var(--rule);font-size:14px;letter-spacing:.5px}
  .brand{display:flex;align-items:center;gap:6px;font-size:13px;letter-spacing:2px;margin-right:10px}
  .brand-dot{width:9px;height:9px;border-radius:50%;background:var(--ink)}
  .page-title{text-align:center;font-size:27px;font-weight:400;margin-top:14px;letter-spacing:.5px}
  .page-subtitle{text-align:center;font-size:19px;margin-top:12px}
  .athletik-graphic{position:absolute;left:170px;top:182px;width:240px;height:340px}
  .athletik-copy{position:absolute;left:570px;top:272px;width:560px;font-size:13px;line-height:1.35}
  .athletik-copy p+p{margin-top:80px}
  .band{position:absolute;left:0;top:553px;width:1200px;height:160px;background:var(--band)}
  .band svg{position:absolute;left:590px;top:48px}

  .mobile-page{position:absolute;left:0;top:1680px;width:1200px;height:1344px;text-align:center}
  .mobile-brand{display:inline-flex;align-items:center;gap:10px;margin-top:70px;font-size:22px;letter-spacing:4px}
  .mobile-brand .brand-dot{width:14px;height:14px}
  .mobile-title{font-size:54px;font-weight:400;margin-top:36px;letter-spacing:1px}
  .mobile-subtitle{font-size:34px;margin-top:6px}
  .mobile-graphic{display:block;margin:50px auto 0;width:720px;height:493px}
  .mobile-copy{width:640px;margin:60px auto 0;font-size:26px;line-height:1.4}
</style>
</head>
<body>

<svg class="sprite" aria-hidden="true">
  <defs>
    <symbol id="pt-graphic" viewBox="40 20 440 290">
      <g fill="none" stroke="var(--thin)" stroke-width="1.5">
        <line x1="135" y1="57" x2="272" y2="57"/>
        <line x1="231" y1="113" x2="272" y2="113"/>
        <line x1="246" y1="168" x2="272" y2="168"/>
        <line x1="231" y1="226" x2="272" y2="226"/>
        <line x1="135" y1="280" x2="272" y2="280"/>
      </g>
      <path d="M135 57 A112 112 0 0 1 135 280" fill="none" stroke="var(--line)" stroke-width="5"/>
      <g fill="var(--grey)">
        <circle cx="135" cy="171" r="82"/>
        <rect x="272" y="34" width="194" height="44" rx="22"/>
        <rect x="272" y="90" width="194" height="44" rx="22"/>
        <rect x="272" y="146" width="194" height="44" rx="22"/>
        <rect x="272" y="202" width="194" height="44" rx="22"/>
        <rect x="272" y="257" width="194" height="44" rx="22"/>
      </g>
      <g fill="var(--line)">
        <circle cx="135" cy="57" r="8"/><circle cx="231" cy="113" r="8"/>
        <circle cx="246" cy="168" r="8"/><circle cx="231" cy="226" r="8"/>
        <circle cx="135" cy="280" r="8"/>
      </g>
      <g fill="#fff" text-anchor="middle">
        <text x="136" y="163" font-size="28">PERSONAL</text>
        <text x="136" y="195" font-size="28">TRAINING</text>
        <text x="369" y="63" font-size="21">motivierend</text>
        <text x="369" y="119" font-size="21">individuell</text>
        <text x="369" y="175" font-size="21">flexibel</text>
        <text x="372" y="231" font-size="21">ganzheitlich</text>
        <text x="369" y="286" font-size="21">abwechslungsreich</text>
      </g>
    </symbol>
    <clipPath id="upper-circle"><circle cx="259" cy="466" r="103"/></clipPath>
    <symbol id="athletik-graphic" viewBox="150 358 220 325">
      <circle cx="259" cy="466" r="103" fill="var(--grey)"/>
      <circle cx="261" cy="573" r="103" fill="var(--grey)"/>
      <circle cx="261" cy="573" r="103" fill="var(--grey-dark)" clip-path="url(#upper-circle)"/>
      <g fill="#fff" text-anchor="middle">
        <text x="260" y="448" font-size="15">VERLETZUNGSPRÄVENTION</text>
        <text x="260" y="513" font-size="21">ATHLETIK-</text>
        <text x="260" y="538" font-size="21">TRAINING</text>
        <text x="263" y="600" font-size="15">LEISTUNGSSTEIGERUNG</text>
      </g>
    </symbol>
  </defs>
</svg>

<svg class="infographics" viewBox="0 0 1024 700" role="group" aria-label="Vier Infografiken zu Personal Training und Athletiktraining">
  <use href="#pt-graphic" x="40" y="20" width="440" height="290"/>

  <g class="process-steps">
    <line x1="704" y1="50" x2="704" y2="284" stroke="var(--line)" stroke-width="6"/>
    <g fill="var(--grey)">
      <rect x="704" y="30" width="181" height="40" rx="20"/>
      <rect x="704" y="88" width="177" height="40" rx="20"/>
      <rect x="704" y="147" width="177" height="40" rx="20"/>
      <rect x="704" y="205" width="181" height="40" rx="20"/>
      <rect x="704" y="264" width="183" height="40" rx="20"/>
      <circle cx="704" cy="50" r="26"/><circle cx="704" cy="108" r="26"/>
      <circle cx="704" cy="167" r="26"/><circle cx="704" cy="225" r="26"/>
      <circle cx="705" cy="284" r="26"/>
    </g>
    <g fill="#fff" text-anchor="middle">
      <text x="705" y="60" font-size="30">1</text>
      <text x="704" y="118" font-size="30">2</text>
      <text x="704" y="177" font-size="30">3</text>
      <text x="704" y="235" font-size="30">4</text>
      <text x="706" y="294" font-size="30">5</text>
      <text x="795" y="56" font-size="15">ERSTGESPRÄCH</text>
      <text x="798" y="114" font-size="14">STANDORTBESTIMMUNG</text>
      <text x="793" y="175" font-size="15">ZIELSETZUNG</text>
      <text x="790" y="231" font-size="15">TRAINING</text>
      <text x="789" y="287" font-size="15">ERFOLG</text>
    </g>
  </g>

  <use href="#athletik-graphic" x="150" y="358" width="220" height="325"/>

  <g class="athlete-stairs">
    <path d="M858 412 H884 V655 H858 M858 468 H884 M858 528 H884 M858 591 H884" fill="none" stroke="var(--line)" stroke-width="6"/>
    <g fill="var(--grey)">
      <rect x="760" y="390" width="98" height="45" rx="22.5"/>
      <rect x="715" y="443" width="143" height="50" rx="25"/>
      <rect x="668" y="502" width="190" height="52" rx="26"/>
      <rect x="638" y="564" width="220" height="54" rx="27"/>
      <rect x="585" y="621" width="273" height="56" rx="28"/>
    </g>
    <g fill="#fff" text-anchor="middle" font-size="14">
      <text x="810" y="417">WETTKAMPF</text>
      <text x="788" y="473">VORWETTKAMPF</text>
      <text x="765" y="533">TRAININGSPLANUNG</text>
      <text x="750" y="596">LAISTUNGSTESTS</text>
      <text x="723" y="653">IST-SOLL-ANALYSE</text>
    </g>
  </g>
</svg>

<section class="web-page" aria-label="Webseite Athletik Training">
  <nav class="site-nav">
    <span class="brand"><span class="brand-dot"></span>HB FITCOACHING</span>
    <span>ÜBER MICH</span><span>DIENSTLEISTUNGEN</span><span>PREISE</span><span>REFERENZEN</span><span>KONTAKT</span>
  </nav>
  <h1 class="page-title">ATHLETIK TRAINING</h1>
  <p class="page-subtitle">Ihr Athletik Trainer aus Bern</p>
  <svg class="athletik-graphic" viewBox="150 358 220 325"><use href="#athletik-graphic" x="150" y="358" width="220" height="325"/></svg>
  <div class="athletik-copy">
    <p>Du kannst als Spitzensportler oder ambitionierter Freizeitsportler<br>nur erfolgreich sein, wenn du verletzungsfrei bleibst. Anhand von<br>Leistungstests und einer individuellen Periodisierung bringen wir dich<br>planmässig und zielführend in Topform für den Wettkampf.</p>
    <p>Als diplomierter Konditionstrainer Alpine Sports Academy begleite ich dich gerne auf diesem Weg.</p>
  </div>
  <div class="band">
    <svg width="170" height="120" viewBox="640 385 250 130">
      <path d="M858 412 H884 V520 M858 468 H884" fill="none" stroke="var(--line)" stroke-width="6"/>
      <rect x="760" y="390" width="98" height="45" rx="22.5" fill="var(--grey)"/>
      <rect x="715" y="443" width="143" height="50" rx="25" fill="var(--grey)"/>
      <g fill="#fff" text-anchor="middle" font-size="14">
        <text x="810" y="417">WETTKAMPF</text>
        <text x="788" y="473">VORWETTKAMPF</text>
      </g>
    </svg>
  </div>
</section>

<section class="mobile-page" aria-label="Mobile Startseite Personal Training">
  <div class="mobile-brand"><span class="brand-dot"></span>HB FITCOACHING</div>
  <h2 class="mobile-title">PERSONAL TRAINING</h2>
  <p class="mobile-subtitle">Ihr Personal Trainer aus Bern</p>
  <svg class="mobile-graphic" viewBox="40 20 440 290"><use href="#pt-graphic" x="40" y="20" width="440" height="290"/></svg>
  <p class="mobile-copy">Abwechslungsreiche Trainings welche dich motivieren, Spass machen und Freude bereiten! Erfahre eine gesunde Einstellung zu körperlicher Aktivität und einer bewussten Ernährung. Individuell auf dich und deine Bedürfnisse abgestimmte Trainings.</p>
</section>

</body>
</html>
```